Request for Business Card Design

Hi. My name is Marlena, I am looking for a new business card design for my company, Quillbrook Sensing Systems, LLC. I really like the design you did for Tavel Harvest and was hoping you could do something similar using our full logo and our mark. I am also open to any raised texture design using our mark. I have attached our full logo, which would need to be somewhere on the card, as well as the mark in both outline and full form, as well as our brand colors / guide. The card does not have to be white, as long as our logo and mark appear. I actually like darker colored business cards more, but am open to all options. If you are interested in working with me, please let me know. We would also take the business card design into letterhead design if you can do that.

```html
<!DOCTYPE html>
<html lang="en">
<head>
<meta charset="utf-8">
<title>Business Cards</title>
<link href="https://fonts.googleapis.com/css2?family=Archivo:wght@700&family=Montserrat:wght@500;600&family=Open+Sans:wght@800&display=swap" rel="stylesheet">
<style>
  :root {
    --ink: #1a3349;
    --card: #19334a;
    --accent: #0a9bc1;
    --paper: #ffffff;
    --text-light: #ffffff;
  }
  html, body {
    margin: 0;
    padding: 0;
    width: 1200px;
    height: 1200px;
    overflow: hidden;
    background: var(--paper);
  }
  .sheet {
    position: relative;
    width: 1200px;
    height: 1200px;
  }
  .sheet-title {
    position: absolute;
    top: 118px;
    left: 0;
    width: 100%;
    margin: 0;
    text-align: center;
    font-family: "Open Sans", sans-serif;
    font-weight: 800;
    font-size: 74px;
    letter-spacing: 1px;
    color: var(--ink);
  }
  .card {
    position: absolute;
    top: 312px;
    width: 455px;
    height: 774px;
    background: var(--card);
    overflow: hidden;
  }
  .card-front { left: 121px; }
  .card-back { left: 631px; }

  .accent-disc {
    position: absolute;
    border-radius: 50%;
    background: var(--accent);
  }
  .card-front .accent-disc { width: 244px; height: 244px; left: -122px; top: 441px; }
  .card-back .disc-top { width: 420px; height: 420px; left: 200px; top: -102px; }
  .card-back .disc-bottom { width: 412px; height: 412px; left: -160px; top: 476px; }

  .brand {
    position: absolute;
    left: 45px;
    top: 45px;
    display: flex;
    align-items: center;
    gap: 10px;
    font-family: "Montserrat", sans-serif;
    font-weight: 600;
    font-size: 20px;
    color: var(--accent);
  }
  .brand-dot {
    width: 18px;
    height: 18px;
    border-radius: 50%;
    background: var(--accent);
  }
  .person-name {
    position: absolute;
    left: 45px;
    top: 136px;
    margin: 0;
    font-family: "Archivo", sans-serif;
    font-weight: 700;
    font-size: 61px;
    line-height: 64px;
    color: var(--text-light);
  }
  .name-rule {
    position: absolute;
    left: 45px;
    top: 287px;
    width: 137px;
    height: 3px;
    background: var(--accent);
  }
  .person-role {
    position: absolute;
    left: 45px;
    top: 313px;
    margin: 0;
    font-family: "Montserrat", sans-serif;
    font-weight: 600;
    font-size: 13px;
    letter-spacing: 3px;
    color: var(--text-light);
  }
  .contact {
    position: absolute;
    right: 45px;
    top: 616px;
    margin: 0;
    text-align: right;
    font-family: "Montserrat", sans-serif;
    font-weight: 500;
    font-size: 14px;
    line-height: 23px;
    letter-spacing: 2px;
    color: var(--text-light);
    font-style: normal;
  }
</style>
</head>
<body>
<main class="sheet">
  <h1 class="sheet-title">BUSINESS CARDS</h1>

  <section class="card card-front">
    <div class="accent-disc"></div>
    <div class="brand"><span class="brand-dot"></span>Quillbrook</div>
    <h2 class="person-name">UNKNOWN<br>PERSON</h2>
    <div class="name-rule"></div>
    <p class="person-role">OWNER/FOUNDER</p>
    <address class="contact">
      555-014-2286<br>
      hello@quillbrook.example<br>
      48 Fernhollow Lane<br>
      Marrow Bay, ST 10482<br>
      www.quillbrook.example
    </address>
  </section>

  <section class="card card-back">
    <div class="accent-disc disc-top"></div>
    <div class="accent-disc disc-bottom"></div>
  </section>
</main>
</body>
</html>
```